Meadowlark Lane Yoga Facebook Design

"Practice Radiant Movement"

Foundational and sustainable yoga practice to cultivate growth through a variety of anatomy- informed movement patterns. Develop an informative and inspirational connection with the mind, body and spirit, through smart and integrated movement.

-I need a design that is happy and cheerful and attracts children and adults alike. I teach vinyassa based yoga that is sustainable and smart, kid yoga, and chair yoga.

-A movement practic rooted in foundation, core, and expression

- Accessible yoga for a sustained practice. A guided movement practice where one gains information and knowledge of oneself through a mind/body connection. For one feel good physically with a new awareness of their internal radiance that exists in all beings. Physical rejuvenation egnites a light and increases energy to flow through the physical body, which ultimately tranlates into works of kindness for others and out in the world.

Nora Whitfield
Yoga Instructor
MD, Pediatrician
RYT-200
RCYT
Certified yoga teacher for adults and children

Full description:
What is the positioning or mission statement of your company? to guide individuals in a yoga-based safe and sustainable movement practice applicable to all ages and body types. Currently my focus is working with children in daycare and school settings, but my goal is to expand into private yoga practice for adults, and potentially as part of rented space in studios. I hope to find a way to work with children AND adults (so would love for logo to be appealing to both), but current focus is with children based on need and demand in the community. yoga for children also compliments my backround as a pediatrician/neonatologist, and I greatly miss interacting with children. I also want to emphasize a yoga/movement practice that is focused more on what one feels internally through movement. NOT what one looks like asthetically. I believe in removing all mirrors from yoga/movement practice. It should be an experience of movement/poses/yoga through appropriate cueing and education. It is not about the details of how far the knee should bend, or how high the leg should be. Focusing on foudation first, core, then core engagement and ultimately expression of poses/movements. A focus on strength, stability and mobility, not just flexibility, which is the common perception/association with yoga. I also want individuals to learn to be an advocate of their own health. Through guidance, I hope for individuals to connect with their body so they know themselves so well to be able to advocate for themselves in the modern healthcare world. This internal experience and connection is so essential in a world where modern medicine has become a business and it is all about making a dollar. the connection with patients is lost, and individuals need to learn to empower themselves and through their new found voice to be able to articulate what is wrong.
Does your company have a tagline or slogan that should be included with the logo? "Practice Radiant Movement"
What do you hope your company can be known for? Accessible yoga for a sustained practice. A guided movement practice where one gains information and knowledge of oneself through a mind/body connection. For one feel good physically with a new awareness of their internal radiance that exists in all beings. Physical rejuvenation egnites a light and increases energy to flow through the physical body, which ultimately tranlates into works of kindness for others and out in the world.
What color palettes might you prefer? why? love the colors currently chosen
Where will the logo be primarily used? initially business cards, but hopefully future websites, t-shirts, and potentially local magazine adds. Also starting with a small couple of banners for community events in the area. I currently practice as a nomad out of my car :)
Are there any elements you would prefer to see in the logo? Movement. A modern depiction of a human body/figure practicing movement. Hoping to avoid a stereotypical yoga pose per say, just because I want to people to think of it more of a movement practice with yoga roots. Modern yoga. There are elements of breathing and connecting with oneself through the flow of breath and movement, but I do not focus on the meditative/cerebral aspect of the yoga practice. What I teach is almost reaching a meditative state through movement. I personally don't practice, nor resonate with just seated meditation. just not my thing :)
In your opinion, what defines a well-designed logo? curiosity. enough info for individuals to think they know what it means, but want to know more. invokes curiosity, but not too abstract. Reproducible. not too complicated. I want also to invoke a community feel, so a design that appeals to all people within a community.
What is your preference in reference to icons, typography, spokespeople (characters), etc.? modern design. I love the idea of a logo for my purposes, to invoke a sense of movement from within. So not too static.
What words or icons must be included in the logo? movement with yoga roots.
What logos do you like and why? A representation, but not exact. I think some ambiguity is intriguing for others, and also memorable. I want it to be an artistic representation of movement/yoga
What logos do you dislike and why? too busy, too loud.
In your opinion, what is the primary purpose for a logo? association
Who is the primary target audience? (who is most likely to use your services/product?) Children and their parents, but ultimately to expand into teaching adults. I even have aspirations of prenatal and post-natal yoga. Potentially incorporating infants.
Who currently uses your product the most? n/a (working in schools/daycare currently. It is currently all volunteer)
Are you pleased with the range of people your company serves? n/a
Are you looking to expand, modify, or completely change your target audience? or will it remain the same? yes! expand into an adult audience.
How do you plan to focus on your target audience? currently by working through schools and daycares. hopefully ultimately through after school care programs and then offering kid yoga in an existing yoga studio (working on this with Q studio in Ridgeland, currently)
What are your main forms of advertising? word of mouth, schools, daycares. Happy kids talking to their parents about the yoga class they took and happy teachers :)
How do most customers find out about your company?
Which gender are you targeting? All genders! However, with kid yoga, often the maternal individual in the child's life is more involved with decision making as far as extracurricular activities

Target Market(s)

Adults, children and families interested in movement, wellness and fun

Font styles to use
Sans Serif

Requirements
Must have
• ***I meant to emphasize the that "S" figure in my logo is SOOO iimportant to me. My daughter designed it. please highlight the "S" figure if possible******
My logo and the phrase "practice radiant movement"
Same colors as my logo
Feel like movement and fun.
Attracts children and families
Incorporate pieces of my description somehow
Nice to have
• different yoga poses or figures in movement
abstract design
attacts all body types and genders
inclusive

Industry is yoga, movement, wellness
Should not have
• no darkness
want happy and vibrant, inviting

```html
<!DOCTYPE html>
<html lang="en">
<head>
<meta charset="UTF-8">
<title>Meadowlark Lane Yoga – Practice Radiant Movement</title>
<link rel="stylesheet" href="https://fonts.googleapis.com/css2?family=Poppins:wght@400;600;700&display=swap">
<style>
  :root {
    --purple: #7a1fc2;
    --purple-deep: #5e12a8;
    --purple-soft: #9a3ad6;
    --sun: #f2c335;
    --sun-soft: #f7d862;
    --white: #ffffff;
    --page: #f1eef4;
  }
  * { margin: 0; padding: 0; box-sizing: border-box; }
  html, body { width: 1200px; height: 800px; overflow: hidden; }
  body {
    background: var(--page);
    font-family: "Poppins", sans-serif;
    display: flex;
    align-items: center;
    justify-content: center;
  }
  .post {
    position: relative;
    width: 760px;
    height: 760px;
    background: var(--purple);
    overflow: hidden;
  }
  .post__shapes { position: absolute; inset: 0; }
  .brand {
    position: absolute;
    left: 34px;
    top: 40px;
    display: flex;
    align-items: center;
    gap: 12px;
  }
  .brand__dot {
    width: 40px; height: 40px;
    border-radius: 50%;
    background: var(--sun);
  }
  .brand__name {
    color: var(--sun);
    font-weight: 600;
    font-size: 22px;
    line-height: 1.1;
    width: 170px;
  }
  .contact {
    position: absolute;
    right: 26px;
    top: 22px;
    font-size: 11px;
    color: var(--purple-deep);
    font-weight: 600;
  }
  .message {
    position: absolute;
    left: 408px;
    top: 160px;
    width: 320px;
  }
  .message__lead {
    color: var(--white);
    font-weight: 600;
    font-size: 30px;
    line-height: 1.3;
  }
  .message__tagline {
    color: var(--sun);
    font-weight: 700;
    font-size: 30px;
    line-height: 1.5;
  }
  .message__credential {
    margin-top: 34px;
    color: var(--white);
    font-weight: 600;
    font-size: 17px;
    line-height: 1.3;
    padding-bottom: 8px;
    border-bottom: 3px solid var(--white);
    width: 250px;
  }
  .message__body {
    margin-top: 14px;
    color: var(--white);
    font-size: 11.5px;
    line-height: 1.5;
    width: 270px;
  }
  .cta {
    display: inline-block;
    margin-top: 50px;
    background: var(--white);
    color: var(--purple);
    font-weight: 700;
    font-size: 13px;
    letter-spacing: 0.06em;
    padding: 12px 0;
    width: 290px;
    text-align: center;
    border-radius: 30px;
  }
  .figures {
    position: absolute;
    left: 20px;
    top: 370px;
    width: 330px;
    height: 330px;
    border-radius: 40%;
    background: radial-gradient(circle at 50% 50%, #e9866f 0%, #c44a8c 45%, rgba(196,74,140,0) 72%);
  }
</style>
</head>
<body>
  <main class="post">
    <svg class="post__shapes" viewBox="0 0 760 760" aria-hidden="true">
      <path d="M330 0 C370 60 430 60 520 30 C610 0 680 40 760 110 L760 0 Z" fill="var(--sun)"/>
      <path d="M470 0 C520 40 600 40 680 20 C720 10 745 30 760 50 L760 0 Z" fill="var(--sun-soft)"/>
      <path d="M0 320 C110 300 180 360 230 430 C280 510 330 560 420 600 C480 630 500 700 470 760 L0 760 Z" fill="var(--sun)"/>
      <path d="M420 760 C520 700 640 690 760 610 L760 760 Z" fill="var(--purple-deep)"/>
      <path d="M0 240 C60 250 110 280 130 320 C80 300 40 300 0 320 Z" fill="var(--purple-soft)"/>
    </svg>

    <div class="brand">
      <span class="brand__dot"></span>
      <span class="brand__name">Meadowlark Lane Yoga</span>
    </div>
    <p class="contact">hello@meadowlarkyoga.com</p>

    <div class="figures" role="img" aria-label="Illustration of an adult and two children doing yoga poses together"></div>

    <section class="message">
      <p class="message__lead">Stay healthy</p>
      <p class="message__tagline">Practice<br>Radiant Movement</p>
      <p class="message__credential">Certified Yoga Teacher<br>for Adults and Children</p>
      <p class="message__body">Foundational and sustainable yoga practice to cultivate growth through a variety of anatomy-informed movement patterns.</p>
      <span class="cta">JOIN US NOW</span>
    </section>
  </main>
</body>
</html>
```